Creating a page for our Spanish tutoring service

We recently launched a new service and would like to create new "solutions" pages to add to our website.

Previously, we provided private one-on-one Spanish tutoring. Now, we are also providing group classes.

We have two documents with some basic copy on each offering. Our website is nice and does not require changes currently, but we do not have the internal bandwidth to build these pages. You would be using our existing design elements to build these two web pages.

Repurposing/copying blocks from our other pages is fine! We have a developer, so design only is required. If you do a good job on this first project, we will have many more pages and projects for you to do!

Our website is tutorlumo.com. TIA for any applicants.

---

Private classes copy:
https://files.quornbay.net/d/7kRtPw2mXa9vLq4ZsNe8Hb3uYc6Tf1Gd/view

Group classes copy:
https://files.quornbay.net/d/3pVxJh5nQe2WsKd8RmTa4YbLc9Uf7Zog/view

Target Market(s)

Online Spanish tutoring and online Spanish classes. We are a very high quality, yet affordable service. Our unique selling proposition is that we operate a completely remote team.

Current customers are typically well-to-do parents or professionals who want to learn Spanish for fun or personal development. They are usually in an okay standing financially (or want to be).

Those who pay for their kids to take lessons want them to have a better future or communicate with their families. Those who are young typically subscribe because they want a better future for themselves. Those who are 30+ years old learn for leisure, travel, or for ongoing professional development.

They want a quality product without paying the high costs associated with in-person tutoring, which is significantly more expensive. They also want to avoid cheaper solutions that are low cost but conversely low quality.

Number of Pages Required

2 page

Font styles to use
Other font styles liked:
• Avenir is our font

Requirements
Must have
• A look and feel consistent with the rest of our website.

```html
<!DOCTYPE html>
<html lang="en">
<head>
<meta charset="utf-8">
<title>TutorLumo – Private and Group Classes</title>
<link rel="stylesheet" href="https://fonts.googleapis.com/css2?family=Poppins:wght@700;800&family=Nunito+Sans:wght@400;600;700&display=swap">
<style>
:root{
  --stage:#666666;
  --teal:#52b7ab;
  --teal-soft:#d9efec;
  --orange:#ff7f3f;
  --ink:#4a4a4a;
  --ink-soft:#7a7a7a;
  --white:#ffffff;
  --band:#f1f6f6;
  --cream:#f6f2ee;
  --rule:#e3e3e3;
}
*{margin:0;padding:0;box-sizing:border-box}
html,body{width:883px;height:1200px;overflow:hidden;background:var(--stage)}
body{position:relative;font-family:"Nunito Sans",Arial,sans-serif;color:var(--ink)}
.brand-title{position:absolute;top:74px;left:0;width:883px;text-align:center;font-family:Poppins,Arial,sans-serif;font-weight:800;font-size:78px;letter-spacing:1px;color:#f3f3f3;line-height:1}
.section-label{position:absolute;top:220px;font-family:Poppins,Arial,sans-serif;font-weight:800;font-size:22px;color:#f3f3f3;line-height:1}
.section-label.private{left:135px}
.section-label.group{left:460px}

.page{position:absolute;top:253px;width:287px;height:843px;background:var(--white);box-shadow:0 6px 14px rgba(0,0,0,.35);overflow:hidden}
.page.private{left:136px}
.page.group{left:460px}
.page > *{position:absolute}

.hero-band{top:0;left:0;width:287px;height:135px;background:var(--teal)}
.site-logo{top:9px;left:21px;font-size:3.6px;font-weight:700;color:var(--white);letter-spacing:.3px}
.site-logo.dark{color:var(--teal)}
.nav{top:10px;left:87px;display:flex;gap:9px;font-size:2.6px;font-weight:700;color:var(--white);letter-spacing:.2px}
.btn-start{top:8px;left:230px;width:35px;height:7px;border-radius:4px;background:var(--orange);color:var(--white);font-size:2.4px;font-weight:700;display:flex;align-items:center;justify-content:center}
.hero-title{left:21px;width:110px;font-weight:700;font-size:5.6px;line-height:6.6px;color:var(--white)}
.hero-sub{left:21px;width:110px;font-size:2.6px;line-height:3.6px;color:var(--white)}
.btn-free{left:21px;width:42px;height:9px;border-radius:5px;background:var(--white);color:var(--ink);font-size:2.6px;font-weight:700;display:flex;align-items:center;justify-content:center}
.photo-frame{top:27px;left:143px;width:122px;height:129px;background:var(--white);padding:4px;box-shadow:0 3px 8px rgba(0,0,0,.18)}
.photo{width:100%;height:100%}
.photo.private-photo{background:linear-gradient(135deg,#e9e6e1,#c9b8a6 45%,#8a7561)}
.photo.group-photo{background:linear-gradient(135deg,#d8d6d2,#b9aa99 50%,#6f6a66)}

.h-section{left:0;width:287px;text-align:center;font-size:7.4px;color:var(--ink)}
.feature{top:190px;width:80px;text-align:center}
.feature svg{display:block;margin:0 auto;width:28px;height:17px}
.feature h3{margin-top:5px;font-size:4.3px;font-weight:600;color:var(--ink)}
.feature p{margin-top:3px;font-size:2.8px;line-height:4.8px;color:var(--ink-soft)}
.rule{top:260px;left:21px;width:244px;height:1px;background:var(--rule)}

.why{left:21px;width:125px}
.why h2{font-size:5.2px;font-weight:400;color:var(--ink);margin-bottom:3px}
.why p{font-size:2.8px;line-height:4.6px;color:var(--ink)}
.why-item{display:flex;gap:4px;margin-top:6px}
.why-num{flex:none;width:8px;height:8px;border-radius:50%;background:var(--teal);color:var(--white);font-size:3.4px;font-weight:700;display:flex;align-items:center;justify-content:center}
.why-item h4{font-size:3.2px;color:var(--teal);font-weight:700;margin-bottom:1px}
.tablet-art{top:272px;left:166px;width:100px;height:170px;background:radial-gradient(ellipse at 50% 45%,#2e2e2e 0 38%,transparent 39%),linear-gradient(180deg,#fff 0%,#e4f3f1 40%,#f3d7c4 100%)}

.testimonial-band{top:444px;left:0;width:287px;height:155px;background:var(--band)}
.testimonial{top:477px;width:70px}
.video{width:70px;height:38px;background:linear-gradient(135deg,#4a4f55,#8b7a6c);position:relative}
.video .caption{position:absolute;top:3px;left:4px;font-size:2.5px;color:var(--white)}
.video .play{position:absolute;left:29px;top:15px;width:11px;height:8px;border-radius:2px;background:rgba(0,0,0,.75)}
.video .play::after{content:"";position:absolute;left:4.5px;top:2px;border-left:3px solid var(--white);border-top:2px solid transparent;border-bottom:2px solid transparent}
.testimonial .name{margin-top:4px;font-size:3.2px;color:var(--ink)}
.testimonial .role{font-size:2.3px;color:var(--ink-soft)}
.testimonial .quote{margin-top:9px;font-size:2.6px;line-height:5.3px;color:var(--ink-soft)}

.press{top:639px;left:40px;width:210px;display:flex;justify-content:space-between;align-items:center;font-weight:700;color:#b3b3b3}
.press span:nth-child(1){font-size:9px}
.press span:nth-child(2){font-size:8px}
.press span:nth-child(3){font-size:4px;letter-spacing:.3px}
.press span:nth-child(4){font-size:4px;letter-spacing:.8px;font-weight:400}
.reviews{top:656px;left:0;width:287px;text-align:center;font-size:2.6px;color:var(--ink)}
.reviews b{color:var(--ink)}
.reviews i{display:inline-block;width:3px;height:3px;background:var(--teal);margin:0 1px 0 3px;vertical-align:-.3px}

.cta-band{top:685px;left:0;width:287px;height:78px;background:var(--teal)}
.cta-title{top:710px;left:21px;width:150px;font-size:7px;line-height:9px;color:var(--white)}
.cta-sub{top:731px;left:21px;width:145px;font-size:2.6px;line-height:4.4px;color:var(--white)}
.btn-cta{top:717px;left:188px;width:77px;height:13px;border-radius:7px;background:var(--orange);color:var(--white);font-size:2.6px;font-weight:700;display:flex;align-items:center;justify-content:center}

.footer-band{top:763px;left:0;width:287px;height:80px;background:var(--cream)}
.foot-col{top:775px;font-size:2.6px;line-height:5px;color:var(--ink-soft)}
.foot-col b{display:block;font-size:3px;color:var(--ink);font-weight:700}
.socials{top:799px;left:227px;display:flex;gap:2px}
.socials i{display:block;width:6px;height:6px;border-radius:50%}
.copyright{top:823px;left:69px;font-size:2.4px;color:var(--ink-soft);display:flex;gap:3px;align-items:center}
.copyright .site-logo{position:static;font-size:3.6px}
.copyright u{color:#3b5bdb}
</style>
</head>
<body>

<div class="brand-title">TUTORLUMO</div>
<div class="section-label private">PRIVATE CLASSES</div>
<div class="section-label group">GROUP CLASSES</div>

<!-- Private classes page -->
<section class="page private">
  <div class="hero-band"></div>
  <div class="site-logo">TUTORLUMO</div>
  <nav class="nav"><span>HOW IT WORKS</span><span>TEACHERS</span><span>TESTIMONIALS</span><span>PRICING</span><span>ABOUT US</span></nav>
  <div class="btn-start">GET STARTED</div>

  <h1 class="hero-title" style="top:40px">Award-Winning Online Spanish Tutoring</h1>
  <p class="hero-sub" style="top:55px">Expert online Spanish tutoring for all levels</p>
  <h2 class="hero-title" style="top:67px">Accelerated learning with online Spanish tutoring</h2>
  <p class="hero-sub" style="top:83px">Learn fast and effectively with fun and engaging private Spanish classes</p>
  <div class="btn-free" style="top:100px">TRY A FREE CLASS</div>
  <div class="photo-frame"><div class="photo private-photo" role="img" aria-label="Photo of three students studying together around a laptop"></div></div>

  <h2 class="h-section" style="top:172px">Key Features</h2>
  <div class="feature" style="left:18px">
    <svg viewBox="0 0 28 17" fill="none" stroke="#52b7ab" stroke-width=".6"><circle cx="20" cy="8.5" r="5" fill="#d9efec" stroke="none"/><rect x="7" y="1" width="11" height="8"/><line x1="9" y1="4" x2="16" y2="4"/><line x1="9" y1="6" x2="14" y2="6"/><circle cx="6" cy="10" r="2"/><path d="M3 16v-2.5a3 3 0 0 1 6 0V16"/></svg>
    <h3>Expert Teachers</h3>
    <p>TutorLumo teachers are trained in the science of teaching Spanish &amp; have worked thousands of hours helping Spanish learners globally.</p>
  </div>
  <div class="feature" style="left:103px">
    <svg viewBox="0 0 28 17" fill="none" stroke="#52b7ab" stroke-width=".6"><circle cx="20" cy="8.5" r="5" fill="#d9efec" stroke="none"/><rect x="8" y="1" width="12" height="7"/><circle cx="9" cy="11" r="1.5"/><circle cx="14" cy="11" r="1.5"/><circle cx="19" cy="11" r="1.5"/><line x1="6" y1="14" x2="22" y2="14"/><line x1="8" y1="14" x2="8" y2="16"/><line x1="20" y1="14" x2="20" y2="16"/></svg>
    <h3>Dedicated Attention</h3>
    <p>Accelerate your learning with one-on-one classes featuring a curriculum that's custom built for your unique needs and interests</p>
  </div>
  <div class="feature" style="left:188px">
    <svg viewBox="0 0 28 17" fill="none" stroke="#52b7ab" stroke-width=".6"><circle cx="20" cy="8.5" r="5" fill="#d9efec" stroke="none"/><line x1="14" y1="2" x2="14" y2="16"/><path d="M11 4l3-3 3 3"/><path d="M14 9l-5-3M7 5l2 1-1 2"/><path d="M14 9l5-3M21 5l-2 1 1 2"/></svg>
    <h3>Flexible &amp; Convenient</h3>
    <p>Online tutoring allows you to learn whenever, and wherever. Find time to continue learning, even if you have a tight schedule.</p>
  </div>
  <div class="rule"></div>

  <div class="why" style="top:299px">
    <h2>Why Private Spanish Tutoring?</h2>
    <p>Fast-track your language learning using online Spanish classes with a dedicated teacher. Get an effective curriculum that's built around your specific goals and current level of comprehension.</p>
    <h2 style="margin-top:8px">What kinds of classes can you expect?</h2>
    <p>Fast-track your language learning using online Spanish classes with a dedicated teacher. Get an effective curriculum that's built around your specific goals and current level of comprehension.</p>
    <div class="why-item"><span class="why-num">1</span><div><h4>Conversational</h4><p>Want to get ready for conversations in the real world? Lessons on every-day topics can help build your vocabulary in essential areas and help you build more confidence speaking.</p></div></div>
    <div class="why-item"><span class="why-num">2</span><div><h4>Grammar</h4><p>Learn the basics or perfect your grammar for use in personal or professional settings. Our grammar-oriented lessons will build you vocabulary while helping you speak perfectly like a native</p></div></div>
  </div>
  <div class="tablet-art" role="img" aria-label="Illustration of a hand holding a tablet showing an online Spanish classes review video"></div>

  <div class="testimonial-band"></div>
  <h2 class="h-section" style="top:462px">What our students say</h2>
  <div class="testimonial" style="left:27px">
    <div class="video" role="img" aria-label="Video thumbnail of a student testimonial"><span class="caption">Hear what Dan has to ...</span><span class="play"></span></div>
    <div class="name">Dan Whitfield</div><div class="role">Learning to socialize</div>
    <p class="quote">"The main things to note are the availability and patience of the teachers. Having them available pretty much on standby, and willing to work with me at my speed, ensured a really got enough practice with each subject to feel comfortable before moving on."</p>
  </div>
  <div class="testimonial" style="left:109px">
    <div class="video" role="img" aria-label="Video thumbnail of a student testimonial"><span class="caption">Hear Why Harper Loves...</span><span class="play"></span></div>
    <div class="name">Harper</div><div class="role">Learning for for travel</div>
    <p class="quote">"On our first call, my teacher interviewed me to find out what I needed to learn. They used this to create custom class plans and help me get basic conversational skills down. I love Spanish music so I asked her if we could go over some well known songs to start with. This was super cool and helped me having fun while learning Spanish!"</p>
  </div>
  <div class="testimonial" style="left:190px">
    <div class="video" role="img" aria-label="Video thumbnail of a student testimonial"><span class="caption">Learn Spanish Online...</span><span class="play"></span></div>
    <div class="name">Imogen</div><div class="role">Learning for music</div>
    <p class="quote">"As I was traveling solo, I really wanted to be able to at least take care of everyday life stuff in Mexico. My schedule did not allow me to actually go to a course though. TutorLumo was great because I could just hop on pretty much instantly and have a class. This flexibility allowed me to drop the excuse of not having enough time."</p>
  </div>

  <h2 class="h-section" style="top:621px">We've been in the News</h2>
  <div class="press"><span>Venture</span><span>Ledger</span><span>DAILY POST</span><span>MARKET BRIEF</span></div>
  <div class="reviews">Check our reviews <u>here</u> <i></i><b>Reviewly</b></div>

  <div class="cta-band"></div>
  <h2 class="cta-title">Group classes are also available OR Try group classes instead</h2>
  <p class="cta-sub">Led by our certified teachers, group classes give learners the opportunity to have real, interactive conversations in Spanish with their peers.</p>
  <div class="btn-cta">LEARN MORE ABOUT GROUP CLASSES</div>

  <div class="footer-band"></div>
  <div class="foot-col" style="left:23px"><b>Information</b>How It Works<br>Pricing</div>
  <div class="foot-col" style="left:64px"><b>Service</b>Teachers<br>Testimonials</div>
  <div class="foot-col" style="left:105px"><b>Company</b>About Us<br>Partner Program</div>
  <div class="foot-col" style="left:145px"><b>Legal</b>Privacy policy<br>Terms of use</div>
  <div class="foot-col" style="left:227px;top:779px"><b>Get in touch</b>Contact Support</div>
  <div class="socials"><i style="background:#3b5998"></i><i style="background:#e02424"></i><i style="background:#d6297a"></i></div>
  <div class="copyright"><span class="site-logo dark">TUTORLUMO</span><span>Copyright © 2020 TutorLumo, Inc. All rights reserved. <u>Privacy Policy</u>. Terms &amp; Conditions.</span></div>
</section>

<!-- Group classes page -->
<section class="page group">
  <div class="hero-band"></div>
  <div class="site-logo">TUTORLUMO</div>
  <nav class="nav"><span>HOW IT WORKS</span><span>TEACHERS</span><span>TESTIMONIALS</span><span>PRICING</span><span>ABOUT US</span></nav>
  <div class="btn-start">GET STARTED</div>

  <h1 class="hero-title" style="top:29px">Learning is fun with online group Spanish classes</h1>
  <p class="hero-sub" style="top:43px;width:115px">Practice together online with real, interactive classes in Spanish</p>
  <h2 class="hero-title" style="top:53px">Learn with friends using online group Spanish classes</h2>
  <p class="hero-sub" style="top:68px">Practice with peers in interactive, online Spanish classes</p>
  <h2 class="hero-title" style="top:78px">Fun and effective group Spanish classes online</h2>
  <p class="hero-sub" style="top:93px">Practice and have conversations with peers in interactive, online Spanish classes</p>
  <div class="btn-free" style="top:109px">TRY A FREE CLASS</div>
  <div class="photo-frame"><div class="photo group-photo" role="img" aria-label="Photo of three students gathered around a laptop"></div></div>

  <h2 class="h-section" style="top:172px">Key Features</h2>
  <div class="feature" style="left:18px">
    <svg viewBox="0 0 28 17" fill="none" stroke="#52b7ab" stroke-width=".6"><circle cx="20" cy="8.5" r="5" fill="#d9efec" stroke="none"/><rect x="7" y="1" width="11" height="8"/><line x1="9" y1="4" x2="16" y2="4"/><line x1="9" y1="6" x2="14" y2="6"/><circle cx="6" cy="10" r="2"/><path d="M3 16v-2.5a3 3 0 0 1 6 0V16"/></svg>
    <h3>Expert Teachers</h3>
    <p>TutorLumo teachers are experts at bringing students together in our group classes, so you can collaborate and improve together</p>
  </div>
  <div class="feature" style="left:103px">
    <svg viewBox="0 0 28 17" fill="none" stroke="#52b7ab" stroke-width=".6"><circle cx="20" cy="8.5" r="5" fill="#d9efec" stroke="none"/><rect x="8" y="3" width="13" height="9"/><line x1="5" y1="14" x2="24" y2="14"/><circle cx="14.5" cy="6.5" r="1.6"/><path d="M12 11a2.5 2.5 0 0 1 5 0"/><rect x="15" y="0.5" width="6" height="3" rx="1"/></svg>
    <h3>Engaging Lessons</h3>
    <p>Pick and choose the classes you want to take by your unique needs and interests. Every class includes fun group activities</p>
  </div>
  <div class="feature" style="left:188px">
    <svg viewBox="0 0 28 17" fill="none" stroke="#52b7ab" stroke-width=".6"><circle cx="20" cy="8.5" r="5" fill="#d9efec" stroke="none"/><rect x="8" y="1" width="12" height="7"/><circle cx="9" cy="11" r="1.5"/><circle cx="14" cy="11" r="1.5"/><circle cx="19" cy="11" r="1.5"/><line x1="6" y1="14" x2="22" y2="14"/><line x1="8" y1="14" x2="8" y2="16"/><line x1="20" y1="14" x2="20" y2="16"/></svg>
    <h3>Unlimited Classes</h3>
    <p>Take as many classes as you'd like. Lock in your spot by scheduling in advance or drop into classes last minute</p>
  </div>
  <div class="rule"></div>

  <div class="why" style="top:297px">
    <h2>Why online Spanish classes?</h2>
    <p>Taking classes in a group settings allows you to</p>
    <h2 style="margin-top:8px">What kinds of classes can you expect?</h2>
    <p>Fast-track your language learning using online Spanish classes with a dedicated teacher. Get an effective curriculum that's built around your specific goals and current level of comprehension.</p>
    <div class="why-item"><span class="why-num">1</span><div><h4>Conversational</h4><p>Want to get ready for conversations in the real world? Lessons on every-day topics can help build your vocabulary in essential areas and help you build more confidence speaking.</p></div></div>
    <div class="why-item"><span class="why-num">2</span><div><h4>Grammar</h4><p>Learn the basics or perfect your grammar for use in personal or professional settings. Our grammar-oriented lessons will build you vocabulary while helping you speak perfectly like a native</p></div></div>
  </div>
  <div class="tablet-art" role="img" aria-label="Illustration of a hand holding a tablet showing an online Spanish classes review video"></div>

  <div class="testimonial-band"></div>
  <h2 class="h-section" style="top:462px">What our students say</h2>
  <div class="testimonial" style="left:27px">
    <div class="video" role="img" aria-label="Video thumbnail of a student testimonial"><span class="caption">Hear what Dan has to ...</span><span class="play"></span></div>
    <div class="name">Dan Whitfield</div><div class="role">Learning to socialize</div>
    <p class="quote">"The main things to note are the availability and patience of the teachers. Having them available pretty much on standby, and willing to work with me at my speed, ensured a really got enough practice with each subject to feel comfortable before moving on."</p>
  </div>
  <div class="testimonial" style="left:109px">
    <div class="video" role="img" aria-label="Video thumbnail of a student testimonial"><span class="caption">Hear Why Harper Loves...</span><span class="play"></span></div>
    <div class="name">Harper</div><div class="role">Learning for for travel</div>
    <p class="quote">"On our first call, my teacher interviewed me to find out what I needed to learn. They used this to create custom class plans and help me get basic conversational skills down. I love Spanish music so I asked her if we could go over some well known songs to start with. This was super cool and helped me having fun while learning Spanish!"</p>
  </div>
  <div class="testimonial" style="left:190px">
    <div class="video" role="img" aria-label="Video thumbnail of a student testimonial"><span class="caption">Learn Spanish Online...</span><span class="play"></span></div>
    <div class="name">Imogen</div><div class="role">Learning for music</div>
    <p class="quote">"As I was traveling solo, I really wanted to be able to at least take care of everyday life stuff in Mexico. My schedule did not allow me to actually go to a course though. TutorLumo was great because I could just hop on pretty much instantly and have a class. This flexibility allowed me to drop the excuse of not having enough time."</p>
  </div>

  <h2 class="h-section" style="top:621px">We've been in the News</h2>
  <div class="press"><span>Venture</span><span>Ledger</span><span>DAILY POST</span><span>MARKET BRIEF</span></div>
  <div class="reviews">Check our reviews <u>here</u> <i></i><b>Reviewly</b></div>

  <div class="cta-band"></div>
  <h2 class="cta-title">Private tutoring is also available OR Try private tutoring instead</h2>
  <p class="cta-sub">Led by our certified teachers, group classes give learners the opportunity to have real, interactive conversations in Spanish with their peers.</p>
  <div class="btn-cta">LEARN MORE ABOUT PRIVATE TUTORING</div>

  <div class="footer-band"></div>
  <div class="foot-col" style="left:23px"><b>Information</b>How It Works<br>Pricing</div>
  <div class="foot-col" style="left:64px"><b>Service</b>Teachers<br>Testimonials</div>
  <div class="foot-col" style="left:105px"><b>Company</b>About Us<br>Partner Program</div>
  <div class="foot-col" style="left:145px"><b>Legal</b>Privacy policy<br>Terms of use</div>
  <div class="foot-col" style="left:227px;top:779px"><b>Get in touch</b>Contact Support</div>
  <div class="socials"><i style="background:#3b5998"></i><i style="background:#e02424"></i><i style="background:#d6297a"></i></div>
  <div class="copyright"><span class="site-logo dark">TUTORLUMO</span><span>Copyright © 2020 TutorLumo, Inc. All rights reserved. <u>Privacy Policy</u>. Terms &amp; Conditions.</span></div>
</section>

</body>
</html>
```